Business Card for TLK Field Services

Would like a large logo on one side. On the other side, logo on one side and company phone number, address, and email on the other side. I don't have a logo so please create one for us.
Updates
I don't have a logo, so please create one for us.
Target Market(s)
Land Surveying
Industry/Entity Type
Surveyor
Contact Information for Business Card
Would like a large logo on one side. On the other side, logo on one side and company phone number, address, and email on the other side
Requirements
Nice to have
- would like the initials to be incorporated with the logo

```html
<!DOCTYPE html>
<html lang="en">
<head>
<meta charset="utf-8">
<title>TLK Field Services – Business Card</title>
<link rel="stylesheet" href="https://fonts.googleapis.com/css2?family=Lato:wght@400;900&family=Archivo:wght@800&display=swap">
<style>
  :root {
    --backdrop: #d9d9d9;
    --card: #f7f7f6;
    --navy: #1d3f86;
    --ink: #111111;
    --rule: #222222;
    --card-shadow: rgba(0, 0, 0, 0.18);
  }
  * { box-sizing: border-box; margin: 0; padding: 0; }
  html, body {
    width: 1200px;
    height: 900px;
    overflow: hidden;
    background: var(--backdrop);
    font-family: "Lato", Arial, sans-serif;
  }
  .canvas {
    position: relative;
    width: 1200px;
    height: 900px;
  }
  .card {
    position: absolute;
    left: 320px;
    width: 560px;
    height: 320px;
    background: var(--card);
    box-shadow: 0 6px 18px var(--card-shadow);
  }
  .card--front { top: 80px; }
  .card--back { top: 480px; }

  /* Front */
  .front-mark {
    position: absolute;
    top: 70px;
    left: 0;
    right: 0;
    display: flex;
    justify-content: center;
    align-items: center;
    gap: 14px;
  }
  .mark-dot {
    width: 22px;
    height: 22px;
    border-radius: 50%;
    background: var(--navy);
  }
  .mark-name {
    font-family: "Lato", Arial, sans-serif;
    font-weight: 900;
    color: var(--navy);
    line-height: 1;
  }
  .front-mark .mark-name { font-size: 88px; }
  .front-tagline {
    position: absolute;
    top: 196px;
    left: 0;
    right: 0;
    text-align: center;
    font-family: "Archivo", Arial, sans-serif;
    font-weight: 800;
    font-size: 38px;
    letter-spacing: 1px;
    color: var(--ink);
  }

  /* Back */
  .back-mark {
    position: absolute;
    top: 0;
    left: 40px;
    width: 220px;
    height: 100%;
    display: flex;
    justify-content: center;
    align-items: center;
    gap: 10px;
  }
  .back-mark .mark-name { font-size: 70px; }
  .back-mark .mark-dot { width: 18px; height: 18px; }
  .divider {
    position: absolute;
    left: 290px;
    top: 70px;
    width: 1.5px;
    height: 180px;
    background: var(--rule);
  }
  .contact {
    position: absolute;
    left: 318px;
    top: 94px;
  }
  .contact-name {
    font-size: 24px;
    font-weight: 400;
    color: var(--ink);
    line-height: 1.1;
  }
  .contact-role {
    font-size: 17px;
    color: var(--navy);
    margin-bottom: 12px;
  }
  .contact-list { list-style: none; }
  .contact-list li {
    display: flex;
    align-items: center;
    gap: 10px;
    font-size: 17px;
    color: var(--ink);
    line-height: 25px;
  }
  .contact-list svg {
    width: 14px;
    height: 14px;
    fill: var(--navy);
    flex: none;
  }
</style>
</head>
<body>
<main class="canvas">
  <section class="card card--front" aria-label="Card front">
    <div class="front-mark">
      <span class="mark-dot"></span>
      <span class="mark-name">TLK</span>
    </div>
    <p class="front-tagline">FIELD SERVICES</p>
  </section>

  <section class="card card--back" aria-label="Card back">
    <div class="back-mark">
      <span class="mark-dot"></span>
      <span class="mark-name">TLK</span>
    </div>
    <div class="divider"></div>
    <div class="contact">
      <p class="contact-name">Dana Hollis</p>
      <p class="contact-role">Managing Director</p>
      <ul class="contact-list">
        <li>
          <svg viewBox="0 0 16 16" aria-hidden="true"><path d="M3.5 1l2.5 3-1.5 1.8c.9 2 2.6 3.8 4.7 4.7L11 9l3 2.5-1.2 2.8C7.6 14.6 1.4 8.4 1.7 3.2z"/></svg>
          <span>5550 1820 4417</span>
        </li>
        <li>
          <svg viewBox="0 0 16 16" aria-hidden="true"><path d="M1 3h14v10H1z M2.5 4.5L8 9l5.5-4.5z" fill-rule="evenodd"/></svg>
          <span>dana@tlkfield.com</span>
        </li>
        <li>
          <svg viewBox="0 0 16 16" aria-hidden="true"><path d="M1 2h14v9H1z M2.5 3.5v6h11v-6z M5 13h6v1.5H5z" fill-rule="evenodd"/></svg>
          <span>www.tlkfield.com</span>
        </li>
      </ul>
    </div>
  </section>
</main>
</body>
</html>
```